Cedar Row Maintenance and Concierge Flyer

We need a flyer for cedar row maintenance and concierge service. We specialize in and provide residential maintenance and errand services to retired and semi retired persons living in the Lake Norman area. The services we include:
Lighting and plumbing repairs
Ceiling fan installation
Handicap accessories
Locks and security
Picture hanging
Hang blinds
Furniture arrangement / assembly
Pressure washing
Battery Jump start
and more...

Our Concierge services include:
Errand running
Grocery shopping
Wellness Checks
Dog Walk
Garbage Collection
and more...

We offer monthly service agreements and 24/7 access
Call text or e-mail for more information
704.555.0187
1cedarrowmaint@quillpostmail.com

The design should invoke a sense of trust and a customer service driven mission

Target Market(s)

Residential maintenance

Industry/Entity Type

Property Maintenance

Contact Information for Business Card

Derek Halvorsen
48176 Quimby Ferrel Rd.
Cornelius NC 28031
704.555.0187
with uploaded logo

Requirements
Nice to have
• Would like a postcard size flyer. Front and back
Should not have
• No pics of of people wearing hard hats or pics of blueprints. No pics of commercial or industrial maintenance.

```html
<!DOCTYPE html>
<html lang="en">
<head>
<meta charset="utf-8">
<title>Cedar Row Maintenance and Concierge Flyer</title>
<link rel="stylesheet" href="https://fonts.googleapis.com/css2?family=Open+Sans:ital,wght@0,300;0,400;0,600;1,400&display=swap">
<style>
  :root {
    --red: #d7262b;
    --red-soft: #de3337;
    --charcoal: #4a4a4a;
    --charcoal-dark: #2e2f2f;
    --grass: #3f5a2c;
    --white: #ffffff;
    --ink: #5a5a5a;
  }
  * { margin: 0; padding: 0; box-sizing: border-box; }
  html, body { width: 896px; height: 1200px; overflow: hidden; background: var(--white); }
  body { font-family: "Open Sans", Arial, sans-serif; color: var(--white); }
  .flyer { position: relative; width: 896px; height: 1200px; overflow: hidden; }

  .photo-row { position: absolute; left: 0; width: 896px; display: grid; grid-template-columns: 290px 306px 300px; }
  .photo-row.top { top: 0; height: 192px; }
  .photo-row.second { top: 390px; height: 195px; }
  .photo { width: 100%; height: 100%; border-right: 2px solid var(--white); }
  .photo:last-child { border-right: 0; }
  .photo.sink { background: linear-gradient(135deg, #c9d2d6, #8ea4ae 60%, #d2c24c); }
  .photo.caregiver { background: linear-gradient(135deg, #e7ded6, #c7b9ad 55%, #8c7d74); }
  .photo.electrician { background: linear-gradient(135deg, #dfe3e6, #aab4bb 60%, #5b7da2); }
  .photo.grocery { background: linear-gradient(135deg, #8a6a3c, #a3442f 45%, #3c5a2d); }
  .photo.washing { background: linear-gradient(135deg, #9aa4a8, #6f7b80 55%, #c66b2a); }
  .photo.workshop { background: linear-gradient(135deg, #b9c3c9, #7d8c96 55%, #3c4a55); }

  .info-band { position: absolute; top: 192px; left: 0; width: 896px; height: 198px; display: grid; grid-template-columns: 290px 306px 300px; }
  .info-panel { display: flex; flex-direction: column; justify-content: center; padding: 0 22px; }
  .info-panel.offer { background: var(--charcoal); font-size: 14px; line-height: 1.6; text-transform: uppercase; letter-spacing: 0.3px; }
  .info-panel.brand { background: var(--white); align-items: center; flex-direction: row; gap: 12px; padding: 0 18px; }
  .brand-mark { flex: none; width: 30px; height: 30px; border-radius: 50%; background: var(--red); }
  .brand-name { color: var(--ink); font-size: 16px; line-height: 1.3; white-space: nowrap; }
  .info-panel.contact { background: var(--red); font-size: 14px; line-height: 1.6; text-transform: uppercase; }
  .contact .phone, .contact .email { text-transform: none; }
  .contact .email { font-size: 13.5px; }

  .services { position: absolute; top: 585px; left: 0; width: 896px; height: 615px; }
  .services-bg { position: absolute; inset: 0; background: linear-gradient(180deg, var(--charcoal-dark) 0%, #333833 45%, var(--grass) 100%); }
  .house-panel { position: absolute; left: 448px; top: 0; width: 448px; height: 615px; background: linear-gradient(160deg, var(--red) 0%, var(--red-soft) 60%, var(--red) 100%); }

  .services h2 { font-weight: 300; font-size: 36px; line-height: 1.2; text-transform: uppercase; letter-spacing: 0.5px; }
  .services ul { list-style: none; font-style: italic; font-size: 17.5px; line-height: 1.58; }
  .services li::before { content: "\2022"; font-style: normal; margin-right: 14px; }
  .maintenance { position: absolute; left: 52px; top: 40px; }
  .maintenance ul { margin-top: 28px; margin-left: 8px; }
  .concierge { position: absolute; left: 488px; top: 318px; }
  .concierge ul { margin-top: 22px; margin-left: 8px; }
</style>
</head>
<body>
<main class="flyer">
  <section class="photo-row top">
    <div class="photo sink" role="img" aria-label="Gloved hand cleaning a kitchen faucet"></div>
    <div class="photo caregiver" role="img" aria-label="Senior woman with a caregiver at home"></div>
    <div class="photo electrician" role="img" aria-label="Technician installing a ceiling light fixture"></div>
  </section>

  <section class="info-band">
    <div class="info-panel offer">
      <p>We offer monthly service<br>agreements and 24/7 access</p>
    </div>
    <div class="info-panel brand">
      <span class="brand-mark"></span>
      <span class="brand-name">Cedar Row<br>Maintenance &amp; Concierge</span>
    </div>
    <div class="info-panel contact">
      <p>Call text or e-mail<br>for more information</p>
      <p class="phone">704.555.0187</p>
      <p class="email">1cedarrowmaint@quillpostmail.com</p>
    </div>
  </section>

  <section class="photo-row second">
    <div class="photo grocery" role="img" aria-label="Woman shopping in a grocery produce aisle"></div>
    <div class="photo washing" role="img" aria-label="Worker pressure washing a patio"></div>
    <div class="photo workshop" role="img" aria-label="Repairman working at a home workbench"></div>
  </section>

  <section class="services">
    <div class="services-bg" role="img" aria-label="Dark backdrop fading into soft green lawn"></div>
    <div class="house-panel" role="img" aria-label="Red panel with a faint house silhouette graphic"></div>

    <div class="maintenance">
      <h2>Our Maintenance<br>Services Include:</h2>
      <ul>
        <li>Lighting and plumbing repairs</li>
        <li>Ceiling fan installation</li>
        <li>Handicap accessories</li>
        <li>Locks and security</li>
        <li>Picture hanging</li>
        <li>Hang blinds</li>
        <li>Furniture arrangement / assembly</li>
        <li>Pressure washing</li>
        <li>Battery jump start</li>
        <li>and more...</li>
      </ul>
    </div>

    <div class="concierge">
      <h2>Our Concierge<br>Services Include:</h2>
      <ul>
        <li>Errand running</li>
        <li>Grocery shopping</li>
        <li>Wellness Checks</li>
        <li>Dog Walk</li>
        <li>Garbage Collection</li>
        <li>and more...</li>
      </ul>
    </div>
  </section>
</main>
</body>
</html>
```